Spring Exterior Painting Advertisement

Attached is the postcard that we used last year(file - brightquill_318939...vector....pdf.. The information contained will be the same except for it will be updated for use during the spring of 2023.

The second attachment (sept 2021mailer) is another design that we've used in the past.

```html
<!DOCTYPE html>
<html lang="en">
<head>
<meta charset="utf-8">
<title>Summit Ridge Painting – Spring Postcard</title>
<link rel="stylesheet" href="https://fonts.googleapis.com/css2?family=Lobster&family=Source+Sans+3:wght@700&family=Source+Serif+4:wght@400&display=swap">
<style>
  :root {
    --teal-light: #8dd6e2;
    --teal-mid: #6aa9b2;
    --teal-dark: #3c6f72;
    --ink: #222222;
    --ink-soft: #333333;
    --paper: #ffffff;
    --banner-text: #e8f6fb;
  }
  * { margin: 0; padding: 0; box-sizing: border-box; }
  html, body { width: 1200px; height: 800px; overflow: hidden; background: var(--paper); }
  .postcard { position: relative; width: 1200px; height: 800px; background: var(--paper); overflow: hidden; }

  .brand-banner { position: absolute; top: 0; left: 857px; width: 343px; height: 236px; }
  .brand-name {
    position: absolute; top: 18px; right: 28px; text-align: right;
    font-family: "Source Serif 4", Georgia, serif; font-weight: 400;
    color: var(--banner-text); line-height: 1;
  }
  .brand-name .line-1 { display: block; font-size: 64px; letter-spacing: 1px; }
  .brand-name .line-2 { display: block; font-size: 46px; letter-spacing: 2px; margin-top: 8px; }

  .intro {
    position: absolute; top: 152px; left: 72px; width: 1090px;
    font-family: "Source Serif 4", Georgia, serif; font-size: 35.5px; line-height: 43.5px;
    color: var(--ink);
  }

  .services {
    position: absolute; top: 420px; left: 72px; width: 1100px;
    display: grid; grid-template-columns: 675px 1fr; list-style: none;
    font-family: "Lobster", cursive; font-size: 36px; color: var(--ink-soft);
  }
  .services ul { list-style: none; }
  .services li { display: flex; align-items: center; height: 56px; }
  .services .col-right { margin-top: -6px; }
  .services .star { width: 26px; height: 26px; margin-right: 12px; flex: none; }

  .contact-band {
    position: absolute; left: 0; top: 648px; width: 1200px; height: 152px;
    background: linear-gradient(90deg, var(--teal-light) 0%, var(--teal-mid) 45%, var(--teal-dark) 100%);
    font-family: "Source Sans 3", Arial, sans-serif; font-weight: 700; color: var(--paper);
    padding: 14px 0 0 29px;
  }
  .contact-band .company { font-size: 33px; line-height: 40px; letter-spacing: 0.5px; }
  .contact-band .address { font-size: 30px; line-height: 38px; margin-top: 5px; font-style: normal; }
</style>
</head>
<body>
<main class="postcard">
  <div class="brand-banner">
    <svg width="343" height="236" viewBox="0 0 343 236" aria-hidden="true">
      <defs>
        <linearGradient id="bannerFill" x1="0" x2="1" y1="0" y2="0">
          <stop offset="0" stop-color="#8dd6e2"/>
          <stop offset="0.55" stop-color="#6aa9b2"/>
          <stop offset="1" stop-color="#3c6f72"/>
        </linearGradient>
      </defs>
      <polygon points="0,0 343,0 343,130 173,235 0,130" fill="url(#bannerFill)"/>
    </svg>
    <div class="brand-name"><span class="line-1">SUMMIT</span><span class="line-2">PAINTING</span></div>
  </div>

  <p class="intro">Summit Ridge Painting’s local team offers painting and staining for your home’s interior and exterior surfaces. From cement board siding to cedar, our teams get the job done right. Homeowner satisfaction and price transparency is at the heart of our small business serving you for over 20 years!</p>

  <svg width="0" height="0" style="position:absolute" aria-hidden="true">
    <defs>
      <linearGradient id="starFill" x1="0" x2="1" y1="0" y2="0">
        <stop offset="0" stop-color="#8dd6e2"/>
        <stop offset="1" stop-color="#3c6f72"/>
      </linearGradient>
      <symbol id="bullet-star" viewBox="0 0 26 26">
        <polygon points="13,1 15.8,9.5 25,10 17.6,15.6 20.4,25 13,19.4 5.6,25 8.4,15.6 1,10 10.2,9.5" fill="url(#starFill)"/>
      </symbol>
    </defs>
  </svg>

  <div class="services">
    <ul class="col-left">
      <li><svg class="star"><use href="#bullet-star"/></svg>Pressure washing</li>
      <li><svg class="star"><use href="#bullet-star"/></svg>Exterior painting and staining</li>
      <li><svg class="star"><use href="#bullet-star"/></svg>Carpentry</li>
    </ul>
    <ul class="col-right">
      <li><svg class="star"><use href="#bullet-star"/></svg>Interior painting</li>
      <li><svg class="star"><use href="#bullet-star"/></svg>Cabinetry Finishing</li>
      <li><svg class="star"><use href="#bullet-star"/></svg>Color Consultations</li>
    </ul>
  </div>

  <footer class="contact-band">
    <div class="company">SUMMIT RIDGE PAINTING</div>
    <address class="address">18 Harbor Ln. Suite B<br>Lakeview WI 53099</address>
  </footer>
</main>
</body>
</html>
```